Design a New Tennis and Athletic Club- Business cards desired with a wow factor.

Help us find a exciting and useful design for our business.
1. Design should be two-sided made of materials that will last.
2. Eye-popping graphics
3. Space for changeable quotes on the back of our card with our "wolf" program logo.
4. Recolor wolf to match club colors

Target Market(s)

Players parents coaches clients

Industry/Entity Type

Business

Contact Information for Business Card

Lakeshore Court + Wellness
Daniel Pruett
Director of Tennis Operations
2817 Birchmont Ave NE
Grand Rapids Michigan 49318
Office (616) 555-0142
Cell (269) 555-0187
Email dpruett482@mailbox-example.com
Website http://www.lscourtclub.example
Facebook https://www.facebook.example/LSCourtClub

Font styles to use
Serif

Colors
0555a3
f37122
ffffff

Requirements
Must have
• 1.interesting contemporary design,
• 2. 2 sided
• 3. ability to swap out staff information for other trainers and professionals
Nice to have
• 1.Space for changeable quotes on the back of the card
• 2. change wolf logo body to match club color blue
• 3. some white space on card for notes to be written.
Should not have
• boring same old consruction

```html
<!DOCTYPE html>
<html lang="en">
<head>
<meta charset="utf-8">
<title>Lakeshore Court + Wellness — Business Card</title>
<link rel="stylesheet" href="https://fonts.googleapis.com/css2?family=Lato:wght@400;700&family=Nunito+Sans:wght@600;800&display=swap">
<style>
  :root {
    --page: #9a9c9b;
    --card-light: #e9e9eb;
    --navy: #12142c;
    --navy-ink: #1b1d3a;
    --orange: #d2502a;
    --text-light: #e4e4ea;
    --gold: #d8b21e;
  }
  * { margin: 0; padding: 0; box-sizing: border-box; }
  html, body { width: 1105px; height: 1200px; overflow: hidden; }
  body { background: var(--page); position: relative; font-family: "Lato", sans-serif; }

  .card { position: absolute; left: 182px; width: 748px; height: 428px; overflow: hidden; }
  .card--front { top: 118px; background: var(--card-light); }
  .card--back { top: 634px; height: 430px; background: var(--navy); }

  .front-panel { position: absolute; inset: 0; }

  .brand { position: absolute; left: 40px; top: 150px; width: 300px; text-align: center;
           font-family: "Nunito Sans", sans-serif; font-weight: 800; color: var(--navy-ink); }
  .brand__mark { width: 44px; height: 44px; border-radius: 50%; background: var(--navy-ink); margin: 0 auto 22px; }
  .brand__name { font-size: 23px; line-height: 30px; letter-spacing: 0.5px; }

  .contact { position: absolute; left: 432px; top: 58px; color: var(--text-light); }
  .contact__name { font-size: 26px; font-weight: 700; letter-spacing: 0.2px; line-height: 32px; }
  .contact__title { font-size: 18px; font-weight: 700; color: var(--orange); line-height: 22px; }
  .contact__list { list-style: none; margin-top: 24px; }
  .contact__item { display: flex; align-items: center; font-size: 19px; line-height: 24px; }
  .contact__icon { width: 20px; height: 16px; margin-right: 9px; flex: none; fill: var(--orange); }
  .contact__address { display: flex; margin-top: 20px; font-size: 19px; line-height: 25px; }
  .contact__address .contact__icon { margin-top: 4px; height: 20px; }

  .program { position: absolute; left: 0; right: 0; top: 180px; text-align: center; }
  .program__mark { width: 60px; height: 60px; border-radius: 50%; background: #1b6a6c; margin: 0 auto 20px; }
  .program__name { font-family: "Nunito Sans", sans-serif; font-weight: 800; font-size: 40px;
                   letter-spacing: 2px; color: var(--text-light); line-height: 44px; }
  .program__sub { font-family: "Nunito Sans", sans-serif; font-weight: 800; font-size: 40px;
                  letter-spacing: 2px; color: var(--text-light); line-height: 44px; }
  .back-url { position: absolute; left: 0; right: 0; top: 372px; text-align: center;
              font-size: 19px; letter-spacing: 6px; color: var(--text-light); }
</style>
</head>
<body>

<section class="card card--front">
  <svg class="front-panel" width="748" height="428" viewBox="0 0 748 428" aria-hidden="true">
    <path d="M328 0 Q420 214 322 428 L748 428 L748 0 Z" fill="var(--navy)"/>
    <path d="M320 0 Q412 214 314 428" fill="none" stroke="var(--orange)" stroke-width="3"/>
  </svg>

  <div class="brand">
    <div class="brand__mark"></div>
    <div class="brand__name">LAKESHORE COURT<br>+ WELLNESS</div>
  </div>

  <div class="contact">
    <div class="contact__name">DANIEL PRUETT</div>
    <div class="contact__title">Director of Tennis Operations</div>
    <ul class="contact__list">
      <li class="contact__item"><svg class="contact__icon" viewBox="0 0 20 16"><path d="M2 6 Q10 0 18 6 L16 8 L13 6 L7 6 L4 8 Z M5 8 L15 8 L17 15 L3 15 Z"/></svg>616 555-0142</li>
      <li class="contact__item"><svg class="contact__icon" viewBox="0 0 20 16"><rect x="6" y="0" width="9" height="16" rx="2"/><rect x="8" y="2" width="5" height="10" fill="var(--navy)"/></svg>269 555-0187</li>
      <li class="contact__item"><svg class="contact__icon" viewBox="0 0 20 16"><rect x="2" y="3" width="16" height="11"/><path d="M2 3 L10 9 L18 3" stroke="var(--navy)" stroke-width="1.5" fill="none"/></svg>dpruett482@mailbox-example.com</li>
      <li class="contact__item"><svg class="contact__icon" viewBox="0 0 20 16"><circle cx="10" cy="8" r="7"/></svg>www.lscourtclub.example</li>
      <li class="contact__item"><svg class="contact__icon" viewBox="0 0 20 16"><rect x="4" y="2" width="12" height="12"/></svg>/LSCourtClub</li>
      <li class="contact__item"><svg class="contact__icon" viewBox="0 0 20 16"><rect x="4" y="2" width="12" height="12"/></svg>lscourtclub.example</li>
    </ul>
    <div class="contact__address">
      <svg class="contact__icon" viewBox="0 0 20 20"><path d="M10 0 C4 0 2 5 4 9 L10 20 L16 9 C18 5 16 0 10 0 Z"/><circle cx="10" cy="7" r="3" fill="var(--navy)"/></svg>
      <div>2817 Birchmont Ave NE<br>Grand Rapids<br>Michigan 49318</div>
    </div>
  </div>
</section>

<section class="card card--back">
  <div class="program">
    <div class="program__mark"></div>
    <div class="program__name">RIDGEBACK TENNIS</div>
  </div>
  <div class="back-url">www.lscourtclub.example</div>
</section>

</body>
</html>
```